Deliver a professional and engaging investment propsal.

I am appealing to highend smart investors and need a high quality, engaging and formal presentation in PDF.
DropBox: https://www.filemarsh.net/sh/q8wz3kdmv2tanp7/BCxRp4LfWmZq9TnYeJ2sKo7vH?dl=0
Text for project is in Dropbox called New Proposal Final
Along with past much older attempts of this job.
Any additional ideas to enable a better outcome would be appreicated.

```html
<!DOCTYPE html>
<html lang="en">
<head>
<meta charset="utf-8">
<title>Kestrel Ridge Business Park – Investment Proposal</title>
<link rel="stylesheet" href="https://fonts.googleapis.com/css2?family=Montserrat:wght@400;600;700;800&family=Open+Sans:ital,wght@0,400;0,600;0,700;1,400&display=swap">
<style>
:root{
  --cyan:#1eb4ea;
  --cyan-soft:#d6f1fb;
  --charcoal:#2c2f33;
  --charcoal-2:#3a3e43;
  --ink:#3b3f44;
  --muted:#8a9096;
  --paper:#ffffff;
  --stage:#ffffff;
  --rule:#e2e6ea;
}
*{box-sizing:border-box;margin:0;padding:0}
html,body{width:1200px;height:3846px;overflow:hidden;background:var(--stage)}
body{position:relative;font-family:"Open Sans",Arial,sans-serif;color:var(--ink)}
.page{position:absolute;width:480px;height:680px;background:var(--paper);overflow:hidden;box-shadow:0 1px 6px rgba(0,0,0,.18)}
.col-l{left:100px}.col-r{left:620px}.col-c{left:360px}
.row1{top:100px}.row2{top:840px}.row3{top:1580px}.row4{top:2320px}.row5{top:3060px}
.page-no{position:absolute;right:14px;bottom:12px;width:18px;height:15px;background:var(--cyan);color:#fff;font:700 8px/15px "Montserrat",sans-serif;text-align:center}
.heading{font-family:"Montserrat",sans-serif;font-weight:700;color:var(--cyan);font-size:21px;letter-spacing:.5px;text-transform:uppercase}
.body-text{font-size:7.3px;line-height:1.5;color:var(--ink)}
.body-text p{margin-bottom:6px}
.photo{display:block}
.two-col{display:grid;grid-template-columns:1fr 1fr;gap:16px}
ul.bullets{list-style:none}
ul.bullets li{position:relative;padding-left:9px;margin-bottom:5px}
ul.bullets li::before{content:"";position:absolute;left:0;top:4px;width:4px;height:4px;background:var(--cyan)}

/* cover */
.cover{background:var(--charcoal)}
.cover-top{height:150px;background:#eef0f2;text-align:center;padding-top:34px}
.cover-title{font:600 30px "Montserrat",sans-serif;letter-spacing:9px;color:var(--charcoal)}
.cover-sub{font:400 19px "Montserrat",sans-serif;letter-spacing:3px;color:var(--charcoal);margin-top:4px}
.cover-art{position:absolute;top:150px;left:0;width:480px;height:330px}
.cover-headline{position:absolute;top:250px;width:100%;text-align:center;color:#fff}
.cover-headline .big{font:700 46px "Montserrat",sans-serif;letter-spacing:3px}
.cover-headline .small{font:400 17px "Montserrat",sans-serif;letter-spacing:2px;margin-top:2px}
.cover-contact{position:absolute;left:30px;bottom:46px;color:#d9dde0;font-size:8px;line-height:1.6}
.cover-contact strong{color:#fff;font-size:10px;font-family:"Montserrat",sans-serif}
.cover-label{position:absolute;right:30px;bottom:36px;color:#cfd3d6;font:400 13px "Montserrat",sans-serif;letter-spacing:6px}

/* contents */
.contents-tag{position:absolute;left:28px;top:34px;background:var(--cyan);color:#fff;font:700 17px "Montserrat",sans-serif;padding:6px 16px}
.contents-panel{position:absolute;left:28px;right:28px;top:48px;height:372px;background:var(--charcoal-2);padding:60px 26px 0 26px;color:#fff}
.contents-head{text-align:right;font:700 12px "Montserrat",sans-serif;margin-bottom:12px}
.contents-row{display:flex;justify-content:space-between;font:700 8.5px "Montserrat",sans-serif;padding:9px 0;letter-spacing:.3px}
.contents-fade{position:absolute;left:0;right:0;bottom:0;height:260px;background:linear-gradient(180deg,#fff 0%,#e7eef3 45%,#cfdde6 100%)}

/* proposal */
.options{margin:8px 0 0;background:var(--cyan-soft);padding:12px 14px}
.options h3{text-align:center;font:700 12px "Montserrat",sans-serif;color:var(--charcoal);letter-spacing:1px;margin-bottom:9px}

/* dark header pages */
.dark-top{background:var(--charcoal);color:#fff;padding:26px 26px 16px}
.dark-top .body-text{color:#e8eaec}
.article-card{background:#fff;height:92px}
.caption{font-size:6.5px;text-align:center;color:#e2e5e8;margin-top:5px;line-height:1.35}

/* table */
.sens-table{width:100%;border-collapse:collapse;font-size:6.2px;margin-top:12px}
.sens-table td{border:1px solid #b9dced;padding:2px 4px;text-align:right;background:#eaf6fc}
.sens-table td:first-child{text-align:right;width:42%}
.sens-table tr.head td{background:#cdebf8;font-weight:600}
.sens-table tr.key td{background:#cdebf8;font-weight:700}

/* team */
.team-sub{font-style:italic;color:var(--cyan);font-size:8px;margin:6px 0 3px}
.conclusion{background:var(--cyan);color:#fff;padding:12px 28px 14px;margin:10px 0}
.conclusion h3{font:700 10px "Montserrat",sans-serif;margin-bottom:6px}
.conclusion p{font-style:italic;font-size:7.3px;line-height:1.5;margin-bottom:6px}
</style>
</head>
<body>

<!-- Page 1: Cover -->
<section class="page cover col-l row1">
  <div class="cover-top">
    <div class="cover-title">KESTREL RIDGE</div>
    <div class="cover-sub">BUSINESS PARK</div>
  </div>
  <svg class="cover-art" viewBox="0 0 480 330" role="img" aria-label="Faded city skyline photograph behind angled cyan panels">
    <defs>
      <linearGradient id="city" x1="0" y1="0" x2="0" y2="1">
        <stop offset="0" stop-color="#5a5f66"/><stop offset="1" stop-color="#2c2f33"/>
      </linearGradient>
    </defs>
    <rect width="480" height="330" fill="url(#city)"/>
    <polygon points="0,0 150,0 0,120" fill="#1eb4ea"/>
    <polygon points="480,0 330,0 480,110" fill="#1eb4ea"/>
    <polygon points="0,90 0,330 190,330" fill="#1eb4ea" opacity=".9"/>
    <polygon points="480,80 480,330 300,330" fill="#1eb4ea" opacity=".9"/>
    <polygon points="60,60 240,40 420,60 400,230 80,230" fill="#ffffff" opacity=".08"/>
  </svg>
  <div class="cover-headline">
    <div class="big">60 ACRE</div>
    <div class="small">MIXED-USE DEVELOPMENT</div>
  </div>
  <div class="cover-contact">
    <strong>Marcus Elden</strong><br>
    m.elden@kestrelridge.example<br>
    Australia<br>
    +61 400 555 218
  </div>
  <div class="cover-label">PROPOSAL</div>
</section>

<!-- Page 2: Contents -->
<section class="page col-r row1">
  <div class="contents-fade" role="img" aria-label="Faded photograph of an open office"></div>
  <div class="contents-panel">
    <div class="contents-head">PAGE</div>
    <div class="contents-row"><span>PROPOSAL</span><span>2</span></div>
    <div class="contents-row"><span>MAJOR SITE CHANGES</span><span>3</span></div>
    <div class="contents-row"><span>LOCATION</span><span>4</span></div>
    <div class="contents-row"><span>ADDITIONAL LOCATION GROWTH</span><span>5</span></div>
    <div class="contents-row"><span>THE PRAIRIE SUMMIT PLUS EXTENDED STAY</span><span>6</span></div>
    <div class="contents-row"><span>SENSITIVITY ANALYSIS</span><span>7</span></div>
    <div class="contents-row"><span>ABOUT OUR QUALITY TEAM</span><span>8</span></div>
    <div class="contents-row"><span>CONCLUSION</span><span>8</span></div>
  </div>
  <div class="contents-tag">CONTENTS</div>
  <div class="page-no">1</div>
</section>

<!-- Page 3: Proposal -->
<section class="page col-l row2" style="padding:26px 28px">
  <h2 class="heading" style="text-align:center;margin-bottom:10px">Proposal</h2>
  <div class="body-text">
    <p>We have an incredible property, Kestrel Ridge Business Park, located at 1180 Prairie Route 9, McKenzie County, Watford City, North Dakota 58854 USA which we have fully funded with cash and now need a joint venture partner, buyer or lender to get the project to completion and producing a substantial profit we all can share.</p>
    <p>Our property is located on the best oil reserves in the world in North Dakota USA, with more oil than any other county in the Bakken Basin and with the lowest recoverable costs of oil per barrel.</p>
    <p>We own the property and need a partner to develop the site and bring to the market at half the cost of competing business parks in this area.</p>
  </div>
  <div class="photo" role="img" aria-label="Photograph of a small town main street at dusk" style="height:100px;margin:6px 0;background:linear-gradient(180deg,#3c5c8e 0%,#6f86a8 45%,#b07a4e 75%,#5a4636 100%)"></div>
  <div class="options">
    <h3>PARTICIPATION OPTIONS</h3>
    <div class="two-col body-text">
      <ul class="bullets">
        <li>A joint venture partner would support all the costs developing the property without the upfront costs of the property purchase.</li>
        <li>All sales would be split to ensure both parties are paid out in such a way that both are paid out in full at the same time from a 50/50 profit share split on all remaining sales.</li>
        <li>Contract drawn up protecting and supporting both parties on agreed terms.</li>
        <li>As a potential joint venture partner, I would cover the full property (57.7 acres) cost as mentioned of $124,790 per acre ($7.2 million).</li>
        <li>Joint venture partner to supply the development costs estimated to be around $650,000 as a staged budget, with tender selection and additional refundable security bonds held with the Watford City development teams.</li>
      </ul>
      <ul class="bullets">
        <li>Development costs could be in up to three stages to lower outlay and limit exposure if so desired, however it will take longer to complete and bring to market.</li>
        <li>A buyer can be fully supported by myself to oversee the full project and outcomes and support the budgets of construction and sales to get the highest returns for a small fee.</li>
        <li>To purchase the property, you would need to contact me directly and I can introduce you to our realtor who will discount his commission from 6% to 3% which is a significant saving.</li>
        <li>Financing on excellent terms allowing 12 to 18 months for income streams and could be linked to a joint venture option or profit share.</li>
      </ul>
    </div>
  </div>
  <div class="page-no">2</div>
</section>

<!-- Page 4: Major site changes -->
<section class="page col-r row2" style="background:var(--charcoal)">
  <div style="padding:26px 26px 10px">
    <h2 class="heading" style="color:#fff;text-align:center;margin-bottom:12px">Major Site Changes</h2>
    <div class="two-col body-text" style="color:#e6e9eb">
      <ul class="bullets">
        <li>We purchased the property in 2013 for cash and without any additional debt, at the time we had highway 85 frontage just outside Watford City limits. South of town with a zoning of agricultural within McKenzie County.</li>
        <li>2014 site zoning changed allowing a commercial zoning.</li>
        <li>Flag Hotel site purchased 2014 now with the option to purchase the franchise license and build the hotel ourselves.</li>
        <li>In 2016 we were added into City Limits which was a massive improvement to our site now taking advantage of confirmed city water and sewer was a great outcome.</li>
        <li>In 2016, the new bypass opened intersecting our highway frontage just 100 yards away which brings all the traffic in the Bakken right past our site which was a massive win for the project.</li>
      </ul>
      <ul class="bullets">
        <li>Same commercial property listed across the road at $750,000 per acre retail at Harlow Commons and other business parks average listings $550,00 per acre.</li>
        <li>In late 2017 we applied for full site development approval which includes all roads and city services, this will trigger interest in the site from passing traffic and with a great marketing campaign will surely start sales coming in quickly once we break ground and start work.</li>
        <li>May 2018 full site infrastructure development approval which includes all roads and city services.</li>
        <li>We can buy the franchise license of the Prairie Summit hotel for additional income potential if desired.</li>
      </ul>
    </div>
  </div>
  <div class="photo" role="img" aria-label="Black and white aerial photograph of the site and the new highway bypass" style="position:absolute;left:0;right:0;bottom:0;height:330px;background:linear-gradient(160deg,#9a9c9e 0%,#6d7073 40%,#8b8d8f 70%,#5c5f62 100%)"></div>
  <div class="page-no">3</div>
</section>

<!-- Page 5: Additional location growth -->
<section class="page col-l row3">
  <div class="dark-top" style="height:360px">
    <h2 class="heading" style="margin-bottom:18px">Additional Location Growth:</h2>
    <div style="display:grid;grid-template-columns:repeat(3,1fr);gap:12px">
      <div>
        <div class="article-card" role="img" aria-label="Screenshot of a news article about a new hotel" style="background:linear-gradient(180deg,#f4f4f4 0 30%,#9fb2c2 30% 100%)"></div>
        <div class="caption">New 150 million dollar Watford City investment 2018</div>
      </div>
      <div>
        <div class="article-card" role="img" aria-label="Screenshot of a news article about oil production" style="background:linear-gradient(180deg,#f4f4f4 0 30%,#b9a98a 30% 100%)"></div>
        <div class="caption">North Dakota is the nation's second biggest oil producer</div>
      </div>
      <div>
        <div class="article-card" role="img" aria-label="Screenshot of a county investment article with a building photo" style="background:linear-gradient(180deg,#2f7fb6 0 30%,#8fb38a 30% 100%)"></div>
        <div class="caption">McKenzie County investment development</div>
      </div>
    </div>
  </div>
  <div class="two-col body-text" style="padding:18px 28px">
    <div>
      <p>Within the 100 yards of Kestrel Ridge Business Park, directly across the road commercial land is currently listed at $750,000 an acre at Harlow Commons and many more locations up to $650,000 per acre. With an advantage over other sites in terms of a better location and much lower purchase and development costs the numbers don't lie and we need to have pad ready to build lots to offer the market.</p>
      <p>Bakken traffic, North, South, East and West will have to travel right by our site making it the second busiest intersection in the Bakken area.</p>
    </div>
    <div>
      <p>giving us the best exposure to sell, promote and grow, this site can and will be the location for new business and growth, we need to develop the site now to move forward.</p>
      <p>With our obvious high exposure to potential buyers through the passing traffic and lower entry price point there is no doubt Kestrel Ridge will become the place where business will want to build alongside a quality business like the Prairie Summit Plus Extended Stay Hotel.</p>
    </div>
  </div>
  <div class="page-no">4</div>
</section>

<!-- Page 6: Location -->
<section class="page col-r row3">
  <div class="photo" role="img" aria-label="Photograph of the town welcome sign" style="height:120px;background:linear-gradient(180deg,#c9d3da 0%,#e4e8ea 55%,#b8a888 100%)"></div>
  <h2 class="heading" style="position:absolute;left:28px;top:100px;background:#fff;padding:4px 10px 2px">Location</h2>
  <div class="two-col body-text" style="padding:22px 28px 0">
    <div>
      <p>Our property is ideally located in Watford City, United States of America, despite its humble beginnings, has suddenly found itself at the epicentre of the Bakken oil boom. Located in Western North Dakota, the City has seen workers flood into the area over recent years to fill positions to support the growth.</p>
      <p>McKenzie County where Watford City is located has more recoverable oil and gas at the lowest recoverable cost per barrel at $24, making it most affordable anywhere in the Bakken basin, centrally located and very desirable area to establish a business and company headquarters.</p>
      <p>Watford City is the crossroads whereby around 20,000 vehicles pass by our site each day travelling locally and between Williston where boom started and Dickinson an established town with network established support for business and infrastructure. Our project has highway frontage and is 100 yards away from the bypass</p>
    </div>
    <div>
      <p>intersection making it the best location in McKenzie County for this type of project.</p>
      <p>With billions invested into infrastructure in the past 5 years in and around the Bakken Shale Oil Basin our project has become the beneficiary of a major new Watford City bypass interchange, Highway 85 just 100 yards south of our project, putting us on one of the busiest intersections in the Bakken. With this rapid growth we were included into the Watford City limits providing additional benefits to the overall success for our development including all city services.</p>
      <p>Demand stems from the ongoing boom in oil and gas drilling in the area which is still in its infancy stages of life, North Dakota oil play and is expected to continue to grow well past 2030 based on obtainable reserves beneath the ground.</p>
    </div>
  </div>
  <div class="photo" role="img" aria-label="Map of North Dakota counties with McKenzie County highlighted in orange" style="position:absolute;left:0;right:0;bottom:0;height:150px;background:linear-gradient(90deg,#e8d9a8 0%,#d8c690 30%,#e0763a 45%,#d9642c 60%,#d8c690 75%,#b9c7d6 100%)"></div>
  <div class="page-no">5</div>
</section>

<!-- Page 7: Prairie Summit Plus -->
<section class="page col-l row4" style="padding:24px 28px">
  <h2 class="heading" style="line-height:1.2;margin-bottom:12px">The Prairie Summit Plus<br>Extended Stay</h2>
  <div class="photo" role="img" aria-label="Photograph of a modern extended stay hotel exterior at dusk" style="height:200px;margin:0 -28px;background:linear-gradient(180deg,#6f8fb6 0%,#9db3cd 35%,#a8583f 60%,#6b4a3c 85%,#3e3b38 100%)"></div>
  <div style="display:grid;grid-template-columns:1fr 1.1fr;gap:14px;margin-top:14px">
    <div class="body-text" style="font-size:8px;line-height:1.55">
      <p>Prairie Summit International's unmatched experience and leadership in the hotel industry designed a new extended stay hotel that satisfy one of the most in-demand needs of today's business and leisure travellers.</p>
      <p>Here guests will experience the very best in hotel and home. Its flexible spaces, stylish design, and brand signature elements come together to create an enriching extended stay experience for your guests, while building loyalty and repeat bookings for your hotel.</p>
    </div>
    <div>
      <div class="photo" role="img" aria-label="Photograph of a hotel suite with a bed and lounge" style="height:115px;background:linear-gradient(135deg,#b99a72,#6e5845)"></div>
      <div class="photo" role="img" aria-label="Photograph of a hotel kitchenette and dining area" style="height:115px;margin-top:8px;background:linear-gradient(135deg,#8f8f84,#4d5a55)"></div>
    </div>
  </div>
  <div class="page-no">6</div>
</section>

<!-- Page 8: Sensitivity analysis -->
<section class="page col-r row4" style="padding:24px 30px">
  <div class="photo" role="img" aria-label="Faded photograph of hands working on financial documents" style="position:absolute;left:0;right:0;bottom:0;height:230px;background:linear-gradient(180deg,#fff 0%,#eef3f6 40%,#d9e4ea 100%)"></div>
  <div style="position:relative">
    <h2 class="heading" style="text-align:center;margin-bottom:10px">Sensitivity Analysis</h2>
    <div class="body-text">
      <p>Sensitivity analysis is based on sales of the full site, (49 saleable acres)</p>
      <p>Our numbers below don't include revenue from build to suit projects or potential income stream from construction of the motel and various projects that could be developed on this 60 acre site. <span style="color:var(--cyan);font-style:italic">These costs are only shown as estimates at this stage.</span></p>
    </div>
    <table class="sens-table">
      <tr class="head"><td>Estimation Projections</td><td>Projected</td><td>Best Scenario</td><td>Worst Scenario</td></tr>
      <tr><td>Average sale per acre (49)</td><td>$450,000</td><td>$500,000</td><td>$300,000</td></tr>
      <tr><td>Total Sales</td><td>$22,050,000</td><td>$24,500,000</td><td>$14,700,000</td></tr>
      <tr class="head"><td>Projected Expenses</td><td></td><td></td><td></td></tr>
      <tr><td>Engineering</td><td>$250,000</td><td>$200,000</td><td>$300,000</td></tr>
      <tr><td>Estimated Site Development Works</td><td>$2,400,000</td><td>$2,000,000</td><td>$4,900,000</td></tr>
      <tr><td>Site Licenses / Permits</td><td>$450,000</td><td>$350,000</td><td>$900,000</td></tr>
      <tr><td>Additional Signage, Marketing</td><td>$150,000</td><td>$100,000</td><td>$300,000</td></tr>
      <tr><td>Professional Fees</td><td>$135,000</td><td>$120,000</td><td>$245,000</td></tr>
      <tr><td>Attorney Cost sale / Support</td><td>$45,000</td><td>$30,000</td><td>$90,000</td></tr>
      <tr><td>Realtor Commissions</td><td>$1,102,500</td><td>$900,000</td><td>$1,200,000</td></tr>
      <tr><td>Property Payout</td><td>$7,200,000</td><td>$7,000,000</td><td>$7,200,000</td></tr>
      <tr class="key"><td>Estimated Projected Full Costs</td><td>$11,732,500</td><td>$10,700,000</td><td>$15,135,000</td></tr>
      <tr><td>Estimated Projected Per Acre Costs</td><td>$239,439</td><td>$218,367</td><td>$308,878</td></tr>
      <tr class="key"><td>Estimated Total Projected Profit</td><td>$10,317,500</td><td>$13,800,000</td><td>-$435,000</td></tr>
      <tr><td>Estimated Profit Each Partner</td><td>$5,158,750</td><td>$6,900,000</td><td>-$217,500</td></tr>
    </table>
    <p class="body-text" style="margin-top:12px">This investment may offer an opportunity for a visa into the USA however you will need to undertake your own inquiries.</p>
  </div>
  <div class="page-no">7</div>
</section>

<!-- Page 9: Team and conclusion -->
<section class="page col-c row5" style="padding-top:26px">
  <h2 class="heading" style="text-align:center;margin-bottom:6px">About Our Quality Team</h2>
  <div class="body-text" style="padding:0 28px">
    <div class="team-sub">Owner – Marcus Elden</div>
    <p>I am an investor always seeking great value opportunities.</p>
    <div class="team-sub">Our Meridian Design and Planning Team</div>
    <p>From planning to conceptual design to construction services, our planning department understands the innovative solutions needed for your project needs. Our planners collaborate with other design professions to create innovative solutions for planning projects and other design needs. Meridian designs with nature in mind and creating sustainable solutions to each unique and individual design requirement. Our pursuit is to bring the public a service with solid goals and concepts by challenging old conventions and implementing new life-giving communities and spaces.</p>
    <p>We have experience and capabilities in conceptual project development, master planning, feasibility studies, park and recreational design, urban and land planning.</p>
  </div>
  <div class="conclusion">
    <h3>IN CONCLUSION</h3>
    <p>This is a solid project located in the Bakken on top of the most cost-effective oil reserves anywhere in the Bakken, centrally located for business and with highway frontage and now with the new bypass intersection at our doorstep, it creates an incredible opportunity.</p>
    <p>I would love to have you come on board as partner, our focus is pushing hard and fast to take advantage of the window of opportunity with the weather in March next year and have everything ready to roll and have lots ready for sale before August 2019.</p>
  </div>
  <div class="body-text" style="padding:0 28px">
    <p>Please send all questions and all joint venture proposals to:</p>
    <p style="line-height:1.6"><strong>Marcus Elden</strong><br>email: m.elden@kestrelridge.example<br>Australia<br>+61 400 555 218</p>
  </div>
  <div class="page-no">8</div>
</section>

</body>
</html>
```